Computer consultant business card

Brimlo Software is a newly started computer consulting company. It's a small one-man company that provides mostly Velunix applications but also websites in collaboration with designers. I'm running this company on the side of full time university studies.

I want the final design to be clean and memorable. Be creative! :)

Some inspiration:
http://www.tavelpix.net/design/73519
http://www.tavelpix.net/design/2739566/business-card-design-by-quillbop
http://www.tavelpix.net/design/804613/business-card-design-by-lorvena-brukwaldsen

See attachment for my company logo.
Updates

I would like to thank everyone for submitting! I'll need a couple of days to review and ultimately select a design.

Target Market(s)

Non-technical entrepreneurs and small companies.

Industry/Entity Type

University

Requirements
Must have
• My company logo.
In any way, both colors from my logo.
First- and last name, e-mail and phone number.
Double-sided design.
Nice to have
• Something creative with the symbol in my logo

```html
<!DOCTYPE html>
<html lang="en">
<head>
<meta charset="utf-8">
<title>Brimlo Software – Business Card</title>
<link rel="stylesheet" href="https://fonts.googleapis.com/css2?family=Exo+2:wght@400;500&display=swap">
<style>
  :root {
    --stage: #1c1c1d;
    --card: #0b0b0c;
    --card-edge: #202022;
    --pattern-dark: #141415;
    --pattern-light: #2e2e30;
    --brand-grey: #4a4a4c;
    --brand-blue: #4a78c0;
    --text-grey: #6a6a6d;
  }
  * { box-sizing: border-box; margin: 0; padding: 0; }
  html, body {
    width: 1200px; height: 900px; overflow: hidden;
    background: var(--stage);
    font-family: "Exo 2", "Helvetica Neue", Arial, sans-serif;
  }
  .stage { position: relative; width: 1200px; height: 900px; }

  .card {
    position: absolute;
    width: 525px; height: 300px;
    background: var(--card);
    border: 1px solid var(--card-edge);
    overflow: hidden;
    box-shadow: 0 18px 40px rgba(0,0,0,.55);
  }
  .card--front { left: 105px; top: 120px; }
  .card--back  { left: 570px; top: 480px; }

  /* decorative pattern areas (brand-symbol texture) */
  .texture {
    position: absolute;
    background: linear-gradient(135deg, var(--pattern-light) 0%, var(--pattern-dark) 70%);
  }
  .card--front .texture {
    left: 0; bottom: 0; width: 62%; height: 48%;
    clip-path: polygon(0 0, 72% 0, 100% 100%, 0 100%);
    opacity: .7;
  }
  .card--back .texture {
    inset: 0;
    clip-path: polygon(0 0, 100% 0, 100% 30%, 42% 30%, 30% 100%, 0 100%);
    opacity: .85;
  }

  .brand {
    position: absolute;
    display: flex; align-items: center; gap: 10px;
    font-weight: 500; color: var(--brand-grey);
    letter-spacing: .01em;
  }
  .brand__dot { border-radius: 50%; background: var(--brand-blue); }
  .card--front .brand { right: 120px; top: 58px; font-size: 38px; }
  .card--front .brand__dot { width: 34px; height: 34px; }
  .card--back .brand { left: 150px; top: 110px; font-size: 66px; }
  .card--back .brand__dot { width: 70px; height: 70px; }

  .contact {
    position: absolute; right: 40px; top: 128px;
    text-align: right;
  }
  .contact__name {
    font-size: 23px; font-weight: 500; color: var(--brand-blue);
    letter-spacing: .04em; margin-right: 22px;
  }
  .contact__role {
    font-size: 13px; color: var(--text-grey); margin: 2px 22px 22px 0;
  }
  .contact__line {
    display: flex; justify-content: flex-end; align-items: center; gap: 8px;
    font-size: 13px; color: var(--text-grey); line-height: 1.6;
  }
  .contact__icon { width: 14px; height: 12px; fill: var(--brand-blue); }

  .card--back .web {
    position: absolute; left: 235px; top: 198px;
    font-size: 19px; color: var(--brand-blue); letter-spacing: .2em;
  }
</style>
</head>
<body>
<main class="stage">
  <section class="card card--front" aria-label="Business card front">
    <div class="texture" role="img" aria-label="Faint repeating brand-symbol texture"></div>
    <div class="brand"><span class="brand__dot"></span>brimlo</div>
    <div class="contact">
      <p class="contact__name">JONAH PELL</p>
      <p class="contact__role">Managing Director</p>
      <p class="contact__line">+ (00) 555 018 2244
        <svg class="contact__icon" viewBox="0 0 14 12" aria-hidden="true"><rect x="3" y="0" width="8" height="12" rx="1.5"/></svg>
      </p>
      <p class="contact__line">jonah@brimlo.com.au
        <svg class="contact__icon" viewBox="0 0 14 12" aria-hidden="true"><path d="M0 1h14v10H0z M1 2l6 5 6-5" stroke="#0b0b0c" stroke-width="1"/></svg>
      </p>
    </div>
  </section>

  <section class="card card--back" aria-label="Business card back">
    <div class="texture" role="img" aria-label="Repeating brand-symbol texture"></div>
    <div class="brand"><span class="brand__dot"></span>brimlo</div>
    <p class="web">www.brimlo.com.au</p>
  </section>
</main>
</body>
</html>
```